Wildlife photographer Website

The website is to be a "resume" of pictures and awards won by Nora. Lean heavy to outdoor wildlife.
She will post articles and have ability to interact with fans.

I will add some of her pictures tonight,

Target Market(s)

Terra Quarterly .....anyone looking to hire a wildlife photographer.

Industry/Entity Type

Professional Photography

Contact Information for Business Card

Nora Falkett
4817 Maple Hollow Lane
Columbia MD 21078
443-581-2094
Nora@FernOwlPix.com

Coding

Coded - Design and coding required

Number of Pages Required

5+ page

Requirements
Must have
• New Logo
Nice to have
• Nature, and eye catching graphics

```html
<!DOCTYPE html>
<html lang="en">
<head>
<meta charset="utf-8">
<title>Nora Falkett — Wildlife Photography</title>
<link rel="stylesheet" href="https://fonts.googleapis.com/css2?family=Domine:wght@500&family=Oswald:wght@300;600&family=Poppins:wght@400;500;600&display=swap">
<style>
:root{
  --orange:#fd9a35;
  --orange-soft:#feb468;
  --ink:#1d1d1d;
  --text:#555;
  --white:#fff;
  --black:#000;
  --rule:#e5e5e5;
}
*{box-sizing:border-box;margin:0;padding:0}
html,body{width:1200px;height:3562px;overflow:hidden}
body{position:relative;background:var(--white);font-family:'Poppins',sans-serif;color:var(--ink)}
.abs{position:absolute}
.photo{position:absolute}
.logo{font-family:'Oswald',sans-serif;font-weight:600;font-size:36px;color:var(--orange);letter-spacing:.5px;line-height:1}
.heading{font-family:'Oswald',sans-serif;font-weight:300;font-size:26px;letter-spacing:.5px;text-transform:uppercase;line-height:1}
.btn{position:absolute;display:flex;align-items:center;justify-content:center;background:var(--orange);color:var(--white);border-radius:20px;font-weight:600;font-size:14px;text-transform:uppercase}

/* hero */
.hero{position:absolute;left:0;top:0;width:1200px;height:636px;
  background:linear-gradient(180deg,#5a6d96 0%,#6f82a8 45%,#8b97b3 100%);
  clip-path:polygon(0 0,100% 0,100% 549px,799px 636px,581px 567px,325px 588px,0 549px)}
.nav a{position:absolute;top:34px;font-size:13px;color:var(--white);text-decoration:none}
.nav a.current{color:var(--orange)}
.hero-title{left:62px;top:222px;font-family:'Domine',serif;font-weight:500;font-size:50px;color:var(--white)}
.hero-title span{color:var(--orange)}
.hero-copy{left:62px;top:286px;width:340px;font-size:13px;line-height:19.5px;color:var(--white)}

/* welcome */
.eyebrow{left:625px;top:735px;font-size:11px;font-weight:600;color:var(--orange)}
.welcome-copy{left:625px;width:420px;font-size:12.5px;line-height:19.5px;color:var(--text)}

/* about */
.about-band{left:0;top:1215px;width:712px;height:314px;background:var(--orange)}
.about-copy{left:62px;top:1314px;width:470px;font-size:12px;line-height:19.5px;color:var(--white)}
.about-copy p+p{margin-top:5px}

/* gallery */
.gallery-card{left:224px;top:1656px;width:751px;height:452px;background:var(--white);box-shadow:0 2px 14px rgba(0,0,0,.1)}
.arrow-dot{width:22px;height:22px;border-radius:50%;background:#d8d8d8;display:flex;align-items:center;justify-content:center}

/* contact */
.contact-band{left:488px;top:2241px;width:712px;height:346px;background:var(--orange)}
.field{position:absolute;background:var(--orange-soft);border-radius:2px;color:var(--white);font-size:12px;padding:10px 8px}

/* articles */
.article-title{font-size:13.5px;line-height:22px;font-weight:500;color:var(--ink)}
.tag{font-size:13px;color:var(--orange)}
.date{font-size:11px;color:#777}

/* footer */
.footer{left:0;top:3216px;width:1200px;height:307px;background:var(--black)}
.footer-bar{left:0;top:3523px;width:1200px;height:39px;background:var(--orange);color:var(--white);font-size:11px;display:flex;align-items:center;justify-content:center}
.footer .heading{color:var(--orange);font-size:21px}
.footer-text{font-size:12px;color:var(--white);line-height:19.5px}
.icon-ring{position:absolute;width:34px;height:34px;border:1.5px solid var(--orange);border-radius:50%;display:flex;align-items:center;justify-content:center}
.social{width:32px;height:32px}
</style>
</head>
<body>

<!-- HERO -->
<div class="hero" role="img" aria-label="Red vermilion flycatcher perched on a bare branch against a blue sky"></div>
<div class="abs logo" style="left:62px;top:18px">Nora Falkett</div>
<nav class="nav">
  <a class="current" style="left:524px">Home</a>
  <a style="left:592px">About Me</a>
  <a style="left:682px">Outdoor wildlife</a>
  <a style="left:809px">Outdoor wildlife</a>
  <a style="left:936px">Articles</a>
</nav>
<div class="btn" style="left:1013px;top:24px;width:128px;height:37px;font-size:13px">Contact Us</div>
<h1 class="abs hero-title">Outdoor <span>Wildlife</span></h1>
<p class="abs hero-copy">Lorem Ipsum is simply dummy text of the printing and typesetting industry. Lorem Ipsum is simply dummy text of the printing and typesetting industry.</p>
<div class="btn" style="left:59px;top:365px;width:136px;height:36px">Learn More</div>

<!-- WELCOME -->
<div class="photo" style="left:159px;top:697px;width:300px;height:337px;background:linear-gradient(160deg,#5f6b3a,#8d9657 50%,#6e7a46)" role="img" aria-label="Cedar waxwing among evergreen branches"></div>
<svg class="abs" style="left:473px;top:776px" width="62" height="63" viewBox="0 0 62 63"><polygon points="0,0 62,63 0,63" fill="var(--orange)"/></svg>
<div class="photo" style="left:317px;top:850px;width:247px;height:263px;background:linear-gradient(180deg,#9aa4a8 0%,#c2b8a6 45%,#b39d82 100%)" role="img" aria-label="Small shorebird standing on wet sand"></div>
<div class="abs eyebrow">WELCOME TO</div>
<h2 class="abs heading" style="left:625px;top:763px;font-size:28px">Wildlife Photography Nora Falkett</h2>
<p class="abs welcome-copy" style="top:804px">Lorem Ipsum is simply dummy text of the printing and typesetting industry. Lorem Ipsum has been the industry's standard dummy text ever since the 1500s, when an unknown printer took a galley of type and scrambled it to make a type specimen book.</p>
<p class="abs welcome-copy" style="top:894px">Lorem Ipsum is simply dummy text of the printing and typesetting industry. Lorem Ipsum has been the industry's standard dummy text ever since the 1500s, when an unknown printer took a galley of type and scrambled it to make a type specimen book.</p>
<div class="btn" style="left:625px;top:986px;width:134px;height:37px">Learn More</div>

<!-- ABOUT -->
<div class="abs about-band"></div>
<div class="photo" style="left:675px;top:1177px;width:525px;height:300px;background:linear-gradient(180deg,#6d6a4e 0%,#a08a5c 55%,#8a6f45 100%)" role="img" aria-label="Photographer kneeling beside a cheetah in dry grassland"></div>
<h2 class="abs heading" style="left:62px;top:1274px;color:var(--white)">About Me</h2>
<div class="abs about-copy">
  <p>Lorem Ipsum is simply dummy text of the printing and typesetting industry. Lorem Ipsum has been the industry's standard dummy text ever since the 1500s, when an unknown printer took a galley of type and scrambled it to make a type specimen book.</p>
  <p>It is a long established fact that a reader will be distracted by the readable content of a page when looking at its layout. The point of using Lorem Ipsum is that it has a more-or-less normal distribution of letters, as opposed to using 'Content here, content here', making it look like readable English.</p>
</div>

<!-- GALLERY -->
<h2 class="abs heading" style="left:0;width:1200px;text-align:center;top:1607px">Gallery</h2>
<div class="abs gallery-card"></div>
<div class="photo" style="left:263px;top:1724px;width:374px;height:315px;background:linear-gradient(180deg,#2b4a72,#1d3a63 60%,#243f66)" role="img" aria-label="Three harlequin ducks swimming on dark water"></div>
<div class="photo" style="left:659px;top:1727px;width:278px;height:146px;background:linear-gradient(180deg,#5c4a2e,#7a6a4a 60%,#cfcfc8)" role="img" aria-label="Two gulls resting on water"></div>
<div class="photo" style="left:659px;top:1893px;width:278px;height:146px;background:linear-gradient(160deg,#5a7db0,#9bb5d6 60%,#8c7b68)" role="img" aria-label="Red-headed woodpecker on a branch"></div>
<div class="abs arrow-dot" style="left:214px;top:1871px"><svg width="10" height="10" viewBox="0 0 10 10"><path d="M6.5 1.5 3 5l3.5 3.5" stroke="#fff" stroke-width="1.6" fill="none"/></svg></div>
<div class="abs arrow-dot" style="left:964px;top:1871px"><svg width="10" height="10" viewBox="0 0 10 10"><path d="M3.5 1.5 7 5 3.5 8.5" stroke="#fff" stroke-width="1.6" fill="none"/></svg></div>
<div class="abs" style="left:264px;top:2049px;font-size:12px;color:#555;display:flex;align-items:center;gap:8px">See All Gellary
  <svg width="30" height="10" viewBox="0 0 30 10"><path d="M0 5h28M23 1l5 4-5 4" stroke="#222" stroke-width="1.4" fill="none"/></svg></div>
<svg class="abs" style="left:585px;top:2120px" width="30" height="6"><circle cx="3" cy="3" r="2.6" fill="#666"/><circle cx="14" cy="3" r="2" fill="#ccc"/><circle cx="25" cy="3" r="2" fill="#ccc"/></svg>

<!-- CONTACT -->
<div class="abs contact-band"></div>
<div class="photo" style="left:0;top:2184px;width:525px;height:339px;background:radial-gradient(ellipse at 55% 35%,#9fb3b2 0%,#4d5f5c 40%,#1f2b2a 85%)" role="img" aria-label="Elephant walking through a misty forest with light rays"></div>
<h2 class="abs heading" style="left:593px;top:2296px;color:var(--white);font-size:24px">Contact Us</h2>
<div class="field" style="left:593px;top:2336px;width:224px;height:36px">Name:</div>
<div class="field" style="left:832px;top:2336px;width:226px;height:36px">Email:</div>
<div class="field" style="left:593px;top:2389px;width:224px;height:36px">Phone:</div>
<div class="field" style="left:832px;top:2389px;width:226px;height:36px">Address:</div>
<div class="field" style="left:593px;top:2441px;width:465px;height:89px">Phone:</div>
<div class="abs" style="left:964px;top:2490px;width:85px;height:29px;background:var(--black);color:var(--white);border-radius:15px;font-size:13px;font-weight:600;display:flex;align-items:center;justify-content:center">SEND</div>

<!-- ARTICLES -->
<h2 class="abs heading" style="left:0;width:1200px;text-align:center;top:2662px">Articles</h2>
<div class="photo" style="left:151px;top:2725px;width:412px;height:315px;background:linear-gradient(180deg,#a07a45,#c59a5e 55%,#8c6a3a)" role="img" aria-label="Short-eared owl flying low over golden grass"></div>
<div class="abs" style="left:151px;top:3014px;width:374px;height:64px;background:var(--white)"></div>
<p class="abs article-title" style="left:167px;top:3021px;width:300px">Lorem Ipsum is simply dummy text of the printing and</p>
<div class="abs" style="left:162px;top:3074px;width:38px;height:38px;border-radius:50%;background:linear-gradient(#d9d9d9,#8a8a8a)" role="img" aria-label="Author portrait"></div>
<div class="abs" style="left:216px;top:3082px;font-size:13.5px;font-weight:500;display:flex;gap:14px;align-items:center">Tessa Brandell <span style="color:#444">/</span> <span class="tag" style="font-size:12px;font-weight:400">Birds</span> <span style="color:#444">/</span> <span class="date" style="font-size:12px">1 Apr 2021</span></div>

<div class="abs" style="left:625px;top:2724px;font-size:13.5px;font-weight:500">Featured Articles</div>
<div class="abs" style="left:622px;top:2750px;width:429px;height:2px;background:var(--orange)"></div>

<div class="photo" style="left:623px;top:2782px;width:121px;height:89px;background:linear-gradient(135deg,#6b3b22,#a55e35 50%,#4a5a3a)" role="img" aria-label="Small bird perched on a branch"></div>
<div class="abs" style="left:767px;top:2782px">
  <div class="tag">Articles</div>
  <p class="article-title" style="width:220px;margin-top:3px">Lorem Ipsum is simply dummy text of the printing and</p>
  <div class="date" style="margin-top:2px">1 Apr , 2021</div>
</div>
<div class="abs" style="left:622px;top:2887px;width:429px;height:1px;background:var(--rule)"></div>

<div class="photo" style="left:623px;top:2902px;width:121px;height:90px;background:linear-gradient(180deg,#3c5670,#2a4560 60%,#5d7488)" role="img" aria-label="Black duck swimming on water"></div>
<div class="abs" style="left:767px;top:2902px">
  <div class="tag">Articles</div>
  <p class="article-title" style="width:220px;margin-top:3px">Lorem Ipsum is simply dummy text of the printing and</p>
  <div class="date" style="margin-top:2px">1 Apr , 2021</div>
</div>
<div class="abs" style="left:622px;top:3014px;width:429px;height:1px;background:var(--rule)"></div>

<div class="photo" style="left:623px;top:3029px;width:121px;height:90px;background:linear-gradient(135deg,#6f8f3a,#3e6b35 50%,#c5537a)" role="img" aria-label="Rainbow bee-eater among pink blossoms"></div>
<div class="abs" style="left:767px;top:3029px">
  <div class="tag">Articles</div>
  <p class="article-title" style="width:220px;margin-top:3px">Lorem Ipsum is simply dummy text of the printing and</p>
  <div class="date" style="margin-top:2px">1 Apr , 2021</div>
</div>

<!-- FOOTER -->
<footer class="abs footer">
  <div class="abs logo" style="left:62px;top:62px">Nora Falkett</div>
  <p class="abs footer-text" style="left:62px;top:120px;width:230px">Lorem Ipsum is simply dummy text of the printing and typesetting industry.</p>

  <h3 class="abs heading" style="left:336px;top:73px">Site Map</h3>
  <div class="abs footer-text" style="left:336px;top:110px;line-height:30px">
    <div>- Home</div><div>- About Me</div><div>- Gallery</div><div>- Articles</div><div>- Contact Us</div>
  </div>

  <h3 class="abs heading" style="left:611px;top:73px">Contact Us</h3>
  <div class="icon-ring" style="left:611px;top:104px"><svg width="16" height="16" viewBox="0 0 16 16"><path d="M8 15s5-5.2 5-9A5 5 0 0 0 3 6c0 3.8 5 9 5 9z" fill="none" stroke="var(--orange)" stroke-width="1.4"/><circle cx="8" cy="6" r="1.8" fill="var(--orange)"/></svg></div>
  <div class="abs footer-text" style="left:655px;top:111px">Out in the wilderness</div>
  <div class="icon-ring" style="left:611px;top:158px"><svg width="16" height="16" viewBox="0 0 16 16"><path d="M3.5 1.5l2.5 0 1.2 3.3-1.7 1.2a8 8 0 0 0 4.5 4.5l1.2-1.7 3.3 1.2 0 2.5c0 .8-.7 1.5-1.5 1.5A12 12 0 0 1 2 3c0-.8.7-1.5 1.5-1.5z" fill="var(--orange)"/></svg></div>
  <div class="abs footer-text" style="left:655px;top:166px">443-581-2094</div>
  <div class="icon-ring" style="left:611px;top:211px"><svg width="17" height="13" viewBox="0 0 17 13"><rect x="1" y="1" width="15" height="11" rx="1" fill="var(--orange)"/><path d="M1.5 1.8 8.5 7.5l7-5.7" stroke="#000" stroke-width="1.2" fill="none"/></svg></div>
  <div class="abs footer-text" style="left:655px;top:218px">Nora@FernOwlPix.com</div>

  <h3 class="abs heading" style="left:888px;top:73px">Follow Us</h3>
  <div class="icon-ring social" style="left:888px;top:105px" aria-label="Social profile"></div>
  <div class="icon-ring social" style="left:925px;top:105px" aria-label="Social profile"></div>
  <div class="icon-ring social" style="left:963px;top:105px" aria-label="Social profile"></div>
  <div class="icon-ring social" style="left:1000px;top:105px" aria-label="Social profile"></div>
</footer>
<div class="abs footer-bar">© 2021 Wildlife Photography Nora Falkett-All Rights Reserved</div>

</body>
</html>
```